I need an advertisement graphic made in two different sizes for a golf tournament

I need an ad made in two different sizes, but can be similar, for a golf tournament

The key components are:

See the future stars of the LKR CIRCUIT at the

Fennwick Bay Classic (logo attached)

May 21-24 at Marrowdale Pines Country Club

Admission is free for everyone!

I need it in the following sizes
1302px wide X 1085 px tall
3840px wide x 2160px tall

I have also added a picture of the golf course
If you use colors, stick with the color scheme in the logo

```html
<!DOCTYPE html>
<html lang="en">
<head>
<meta charset="utf-8">
<title>Fennwick Bay Classic – Ad Sizes</title>
<link href="https://fonts.googleapis.com/css2?family=Montserrat:wght@400;600;700;800&family=Saira+Condensed:wght@600;700&display=swap" rel="stylesheet">
<style>
  :root{
    --backdrop:#7a7a7a;
    --navy:#223f56;
    --green:#86c04a;
    --white:#ffffff;
    --caption:#f1f1f1;
    --sky-top:#1f86d0;
    --sky-mid:#5aaee0;
    --cloud:#dfe9f1;
    --ridge:#3a5f7a;
    --forest:#24491c;
    --fairway:#78b532;
    --fairway-light:#8fc63e;
    --fairway-shade:#3f7418;
  }
  *{margin:0;padding:0;box-sizing:border-box}
  html,body{width:1200px;height:904px;overflow:hidden;background:var(--backdrop)}
  .board{position:relative;width:1200px;height:904px}

  .ad{position:absolute;background:var(--navy);overflow:hidden}
  .ad-photo{position:absolute;left:0;top:0;width:100%;
    background:
      radial-gradient(ellipse 40% 12% at 25% 14%, rgba(255,255,255,.75), rgba(255,255,255,0) 100%),
      radial-gradient(ellipse 35% 10% at 55% 22%, rgba(255,255,255,.7), rgba(255,255,255,0) 100%),
      radial-gradient(ellipse 45% 30% at 50% 78%, var(--fairway-light), rgba(143,198,62,0) 100%),
      linear-gradient(180deg,var(--sky-top) 0%,var(--sky-mid) 18%,var(--cloud) 30%,#8fc0e3 36%,var(--ridge) 40%,var(--forest) 46%,#2f5a1f 55%,var(--fairway) 68%,var(--fairway) 84%,var(--fairway-shade) 100%)}
  .ad-logo{position:absolute;top:0;background:var(--white);display:flex;flex-direction:column;align-items:center;justify-content:center;text-align:center}
  .logo-tagline{font-family:"Montserrat",sans-serif;font-weight:600;color:var(--navy);line-height:1.2}
  .logo-name{font-family:"Saira Condensed",sans-serif;font-weight:700;color:var(--navy);text-transform:uppercase;line-height:.95}
  .ad-band{position:absolute;left:0;bottom:0;width:100%;background:var(--navy)}
  .event-info{position:absolute;display:flex;flex-direction:column;align-items:flex-start}
  .event-date{font-family:"Saira Condensed",sans-serif;font-weight:700;color:var(--green);line-height:1;white-space:nowrap}
  .event-venue{font-family:"Montserrat",sans-serif;font-weight:700;color:var(--white);white-space:nowrap}
  .admission{position:absolute;bottom:0;background:var(--white);display:flex;flex-direction:column;align-items:center;justify-content:center;font-family:"Montserrat",sans-serif;color:var(--navy);text-transform:uppercase}
  .admission-top{font-weight:800;line-height:1}
  .admission-free{background:var(--green);color:var(--white);font-weight:800;line-height:1;text-align:center}
  .admission-bottom{font-weight:700;line-height:1;letter-spacing:-.02em}
  .size-caption{position:absolute;left:0;width:1200px;text-align:center;font-family:"Montserrat",sans-serif;font-weight:400;color:var(--caption)}

  /* 1302 x 1085 */
  .ad--small{left:424px;top:35px;width:352px;height:293px}
  .ad--small .ad-photo{height:225px}
  .ad--small .ad-logo{left:230px;width:93px;height:74px;padding:0 5px}
  .ad--small .logo-tagline{font-size:5.6px;margin-bottom:4px}
  .ad--small .logo-name{font-size:15px}
  .ad--small .ad-band{height:68px}
  .ad--small .event-info{left:20px;top:232px}
  .ad--small .event-date{font-size:33px}
  .ad--small .event-venue{font-size:10.6px;margin-top:2px}
  .ad--small .admission{left:230px;width:93px;height:68px}
  .ad--small .admission-top{font-size:12.5px}
  .ad--small .admission-free{font-size:15px;width:74px;padding:2px 0;margin:4px 0 5px}
  .ad--small .admission-bottom{font-size:8.6px}
  .caption--small{top:341px;font-size:15px}

  /* 3840 x 2160 */
  .ad--large{left:195px;top:388px;width:810px;height:456px}
  .ad--large .ad-photo{height:307px}
  .ad--large .ad-logo{left:529px;width:214px;height:131px;padding:0 14px}
  .ad--large .logo-tagline{font-size:11.5px;margin-bottom:8px}
  .ad--large .logo-name{font-size:34px}
  .ad--large .ad-band{height:149px}
  .ad--large .event-info{left:46px;top:318px}
  .ad--large .event-date{font-size:75px}
  .ad--large .event-venue{font-size:25px;margin-top:4px}
  .ad--large .admission{left:529px;width:214px;height:149px}
  .ad--large .admission-top{font-size:31px}
  .ad--large .admission-free{font-size:37px;width:168px;padding:4px 0;margin:8px 0 10px}
  .ad--large .admission-bottom{font-size:22px}
  .caption--large{top:852px;font-size:15px}
</style>
</head>
<body>
<main class="board">

  <section class="ad ad--small" aria-label="Ad, 1302 by 1085">
    <div class="ad-photo" role="img" aria-label="Aerial photo of the golf course fairway lined with trees, green hills and a cloudy blue sky"></div>
    <div class="ad-logo">
      <span class="logo-tagline">See the future stars of the LKR CIRCUIT at the</span>
      <span class="logo-name">Fennwick<br>Bay Classic</span>
    </div>
    <div class="ad-band"></div>
    <div class="event-info">
      <span class="event-date">MAY 21-24, 2026</span>
      <span class="event-venue">at Marrowdale Pines Country Club</span>
    </div>
    <div class="admission">
      <span class="admission-top">Admission</span>
      <span class="admission-free">Is Free</span>
      <span class="admission-bottom">For Everyone!</span>
    </div>
  </section>
  <p class="size-caption caption--small">1302px wide X 1085 px tall</p>

  <section class="ad ad--large" aria-label="Ad, 3840 by 2160">
    <div class="ad-photo" role="img" aria-label="Aerial photo of the golf course fairway lined with trees, green hills and a cloudy blue sky"></div>
    <div class="ad-logo">
      <span class="logo-tagline">See the future stars of the LKR CIRCUIT at the</span>
      <span class="logo-name">Fennwick<br>Bay Classic</span>
    </div>
    <div class="ad-band"></div>
    <div class="event-info">
      <span class="event-date">MAY 21-24, 2026</span>
      <span class="event-venue">at Marrowdale Pines Country Club</span>
    </div>
    <div class="admission">
      <span class="admission-top">Admission</span>
      <span class="admission-free">Is Free</span>
      <span class="admission-bottom">For Everyone!</span>
    </div>
  </section>
  <p class="size-caption caption--large">3840px wide x 2160px tall</p>

</main>
</body>
</html>
```